A professional business to business web site for a contract agency called VONTAREX.

We need a very clean, very professional web site created for business to business. It is an informational web site with 3 pages. We are a company that offers contract employee placements into primarily the pharmaceutical industry. I have attached a file that describes the company more fully.

Hi,

I'm sorry if I wasn't clear, but I need to have the HTML pages created so I can just upload the files you give me to the web hosting site.

Please let me know if you have any questions.

Thanks for working on my project!

Hello,

I didn't put this in the description, but I would need the web site set up on the web hosting site as well.  The web hosting site is abrightkettle.  I want a copy of all the files as well.

Thanks,
Miles

Reason: I'm sorry, unexpectedly, I have been very busy and I haven't been able to devote the time necessary for this. I am extending the deadline by 10 days. Thank you for your patience. Thanks.

Reason: Hi everyone, I apologize again, but everything has been so busy here that I haven't been able to give this attention. I plan to work on this over the next few days. Thanks and sorry again, Miles.

Reason: I'm sorry this is taking longer than planned. I have been extremely busy. I have increased the budget on this project. Thanks.

Target Market(s)

Large professional corporations mainly in the pharmaceutical industry. The audience is hiring decisions makers within the companies and potential job candidates/job seekers.

Industry/Entity Type

Pharmaceutical

Font styles to use
Sans Serif

Requirements
Must have
• Must have a clean look that mimics the pharmaceutical industry web sites. VERY professional.
Nice to have
• A nice picture of professional business/pharma/technical people looking like a team. Colors are listed on the attached Word document.
Should not have
• No animation. Not too busy.

```html
<!DOCTYPE html>
<html lang="en">
<head>
<meta charset="utf-8">
<title>VONTAREX — Companies</title>
<link rel="stylesheet" href="https://fonts.googleapis.com/css2?family=Jura:wght@500&family=Open+Sans:wght@400;600&family=Roboto:wght@400&display=swap">
<style>
  :root {
    --navy: #1b2b86;
    --nav-top: #1d4a9c;
    --nav-bottom: #10277a;
    --banner-frame: #2c0f6c;
    --banner-purple: #4b2590;
    --photo-light: #d7d7d7;
    --page-grey: #e9e9eb;
    --text: #222222;
    --body-text: #3a3a3a;
    --rule: #c8c8cc;
    --white: #ffffff;
  }
  * { margin: 0; padding: 0; box-sizing: border-box; }
  html, body { width: 1200px; height: 1105px; overflow: hidden; }
  body {
    position: relative;
    font-family: Arial, Helvetica, sans-serif;
    color: var(--text);
    background: var(--white);
  }
  .top-area {
    position: absolute; left: 0; top: 0; width: 1200px; height: 566px;
    background: linear-gradient(180deg, #f1f1f3 0%, var(--page-grey) 100%);
  }
  .brand {
    position: absolute; left: 106px; top: 60px;
    display: flex; align-items: center; gap: 10px;
    font-family: "Open Sans", sans-serif; font-weight: 600;
    font-size: 27px; letter-spacing: 5px; color: var(--navy);
  }
  .brand-dot { width: 14px; height: 14px; border-radius: 50%; background: var(--navy); }
  .call {
    position: absolute; right: 121px; top: 64px;
    display: flex; align-items: baseline; gap: 6px;
    font-family: "Roboto", sans-serif; color: var(--text);
  }
  .call svg { align-self: center; }
  .call-label { font-size: 12px; }
  .call-number { font-size: 20px; }
  .main-nav {
    position: absolute; left: 100px; top: 120px; width: 999px; height: 42px;
    border-radius: 4px;
    background: linear-gradient(180deg, var(--nav-top), var(--nav-bottom));
    display: flex;
  }
  .main-nav a {
    font-family: "Open Sans", sans-serif; font-weight: 600; font-size: 15px;
    color: var(--white); text-decoration: none; letter-spacing: 0.3px;
    display: flex; align-items: center; justify-content: center;
    border-right: 1px solid rgba(255,255,255,0.15); height: 42px;
  }
  .main-nav a:last-child { border-right: none; }
  .banner {
    position: absolute; left: 99px; top: 200px; width: 1000px; height: 214px;
    border: 5px solid var(--banner-frame); border-right-width: 6px;
    display: flex; background: var(--banner-frame);
  }
  .banner-title {
    width: 473px; height: 204px; background: linear-gradient(135deg, #5530a0, var(--banner-purple));
    position: relative;
  }
  .banner-title h1 {
    position: absolute; left: 57px; top: 66px;
    font-family: "Open Sans", sans-serif; font-weight: 400; font-size: 56px;
    color: #f2eefb; letter-spacing: 0.5px;
  }
  .banner-photo {
    width: 516px; height: 204px;
    background: linear-gradient(90deg, var(--photo-light), #b8b8b8 50%, var(--photo-light));
  }
  .intro {
    position: absolute; left: 100px; top: 450px; width: 990px;
    text-align: center; font-size: 14.5px; line-height: 22px; color: var(--text);
  }
  .intro .name { color: var(--navy); }
  .services {
    position: absolute; left: 0; top: 566px; width: 1200px; height: 453px;
    background: #fbfcfe;
  }
  .divider-v {
    position: absolute; left: 584px; top: 59px; height: 324px;
    border-left: 1px dotted var(--rule);
  }
  .divider-h {
    position: absolute; left: 99px; top: 212px; width: 968px;
    border-top: 1px dotted var(--rule);
  }
  .service { position: absolute; }
  .service h2 {
    font-family: "Jura", sans-serif; font-weight: 500; font-size: 25.5px;
    color: var(--navy); letter-spacing: 0; white-space: nowrap;
  }
  .service svg { position: absolute; }
  .service p {
    position: absolute; font-size: 13px; line-height: 20px;
    letter-spacing: 0.5px; color: var(--body-text);
  }
  .contact-line {
    position: absolute; right: 123px; top: 423px; font-size: 13.5px; color: var(--text);
  }
  .contact-line a { color: var(--navy); }
  .site-footer {
    position: absolute; left: 0; top: 1019px; width: 1200px; height: 86px;
    background: linear-gradient(180deg, var(--nav-top), var(--nav-bottom));
    color: var(--white); text-align: center; font-size: 13.5px;
  }
  .footer-links { padding-top: 18px; }
  .footer-links a { color: var(--white); text-decoration: none; }
  .copyright { margin-top: 14px; }
</style>
</head>
<body>
  <header class="top-area">
    <div class="brand"><span class="brand-dot"></span>VONTAREX</div>
    <div class="call">
      <svg width="14" height="18" viewBox="0 0 14 18" aria-hidden="true"><path d="M4 1 L7 5 L5 7 C6 10 8 12 10 13 L12 11 L14 14 L11 17 C5 15 1 9 1 4 Z" fill="#2a2a2a"/></svg>
      <span class="call-label">Call Us:</span><span class="call-number">555-014-0392</span>
    </div>
    <nav class="main-nav">
      <a href="#" style="width:130px">HOME</a>
      <a href="#" style="width:155px">COMPANIES</a>
      <a href="#" style="width:159px">CANDIDATES</a>
      <a href="#" style="width:152px">CONTACT US</a>
    </nav>
    <section class="banner">
      <div class="banner-title"><h1>Companies</h1></div>
      <div class="banner-photo" role="img" aria-label="Black and white photo of a smiling team of business professionals holding a molecule model"></div>
    </section>
    <p class="intro"><span class="name">VONTAREX</span> works with large and small companies throughout the nation, including Apex 500 companies, providing people with the right skill set to make businesses and their operations run more effectively.&nbsp; We specialize in the pharmaceutical industry and have contacts throughout the nation that can bring their time and talent to enhance your team.&nbsp; We can work with you on any need but focus primarily in the following areas:</p>
  </header>

  <main class="services">
    <div class="divider-v"></div>
    <div class="divider-h"></div>

    <article class="service" style="left:114px; top:66px;">
      <h2>Project Managers</h2>
      <svg style="left:6px; top:50px" width="64" height="64" viewBox="0 0 64 64" aria-hidden="true">
        <rect x="24" y="2" width="16" height="5" fill="#2a2a2a"/>
        <rect x="1" y="6" width="62" height="6" rx="2" fill="#2a2a2a"/>
        <rect x="6" y="12" width="52" height="40" fill="none" stroke="#2a2a2a" stroke-width="5"/>
        <circle cx="32" cy="32" r="13" fill="#2a2a2a"/>
        <path d="M32 32 L32 22 A10 10 0 0 1 42 32 Z" fill="#fff"/>
        <path d="M14 52 L9 63 M50 52 L55 63" stroke="#2a2a2a" stroke-width="5"/>
      </svg>
      <p style="left:86px; top:49px; width:355px">VONTAREX’s project managers are organizers and executers of your project goals that bring attention to detail, focus on efficiency, and results driven success.</p>
    </article>

    <article class="service" style="left:632px; top:65px;">
      <h2>Application Specialists &amp; Engineers</h2>
      <svg style="left:0; top:51px" width="62" height="52" viewBox="0 0 62 52" aria-hidden="true">
        <rect x="2" y="2" width="58" height="48" rx="3" fill="none" stroke="#2a2a2a" stroke-width="4"/>
        <rect x="7" y="7" width="48" height="36" fill="#2a2a2a"/>
        <rect x="10" y="10" width="42" height="30" fill="#fff"/>
        <path d="M11 25 H22 L25 18 L29 33 L33 21 L36 25 H51" fill="none" stroke="#2a2a2a" stroke-width="2"/>
        <circle cx="8" cy="46" r="1.3" fill="#fff"/><circle cx="12" cy="46" r="1.3" fill="#fff"/>
      </svg>
      <p style="left:82px; top:48px; width:372px">VONTAREX works with Application Specialists and Appli-cation Engineers that can install, configure, and manage laboratory software solutions such as Kestrova, Lumadyne, Orvanta and/or similar software.</p>
    </article>

    <article class="service" style="left:114px; top:238px;">
      <h2>Application Trainers</h2>
      <svg style="left:11px; top:52px" width="52" height="52" viewBox="0 0 52 52" aria-hidden="true">
        <g fill="#2a2a2a">
          <rect x="0" y="0" width="13" height="13" rx="2"/><rect x="19" y="0" width="13" height="13" rx="2"/><rect x="38" y="0" width="13" height="13" rx="2"/>
          <rect x="0" y="19" width="13" height="13" rx="2"/><rect x="19" y="19" width="13" height="13" rx="2"/><rect x="38" y="19" width="13" height="13" rx="2"/>
          <rect x="0" y="38" width="13" height="13" rx="2"/><rect x="19" y="38" width="13" height="13" rx="2"/><rect x="38" y="38" width="13" height="13" rx="2"/>
        </g>
      </svg>
      <p style="left:88px; top:49px; width:325px">VONTAREX’s Application Trainers can demonstrate and train on the latest laboratory software packages.</p>
    </article>

    <article class="service" style="left:632px; top:237px;">
      <h2>Chemists &amp; Laboratory Technicians</h2>
      <svg style="left:4px; top:52px" width="48" height="64" viewBox="0 0 48 64" aria-hidden="true">
        <rect x="14" y="1" width="20" height="5" rx="1" fill="#2a2a2a"/>
        <path d="M17 6 V24 L3 56 Q2 61 8 61 H40 Q46 61 45 56 L31 24 V6" fill="none" stroke="#2a2a2a" stroke-width="3.5"/>
        <path d="M10 42 H38 L43 56 Q43 58 40 58 H8 Q5 58 5 56 Z" fill="#2a2a2a"/>
        <circle cx="20" cy="49" r="3" fill="#fff"/><circle cx="29" cy="52" r="2" fill="#fff"/><circle cx="26" cy="34" r="2" fill="#2a2a2a"/>
      </svg>
      <p style="left:75px; top:46px; width:382px">VONTAREX provides great team members in every position in the laboratory environment.&nbsp; Whether you are a R&amp;D, QC, or other research test facility VONTAREX will work with your company to enhance your company’s success.</p>
    </article>

    <p class="contact-line">Please <a href="#">Contact Us</a> and tell us how we can help enhance your team!</p>
  </main>

  <footer class="site-footer">
    <div class="footer-links"><a href="#">Home</a> &nbsp;| <a href="#">Companies</a> &nbsp;| &nbsp;<a href="#">Candidates</a> &nbsp;| &nbsp;<a href="#">Contact Us</a></div>
    <div class="copyright">Copyright © 2013 &nbsp;VONTAREX . All rights reserved.</div>
  </footer>
</body>
</html>
```